M&A Advisory firm needs elegant and powerful letterhead

We need a powerful but elegant letterhead to engage with the international financial industry.

Target Market(s)

New York and International Financial Industry

Industry/Entity Type

Finance

Font styles to use
Other font styles liked:
• Poppins

Requirements
Must have
• 482 W 71st Street 14th Floor New York, NY 10157 O: +1 (212) 555 0147 F: +1 (212) 555 0182

```html
<!DOCTYPE html>
<html lang="en">
<head>
<meta charset="utf-8">
<title>Kestrow Letterhead</title>
<link href="https://fonts.googleapis.com/css2?family=Poppins:wght@400;500;600;700&display=swap" rel="stylesheet">
<style>
  :root {
    --brand-blue: #0f5493;
    --brand-grey: #808285;
    --paper: #ffffff;
    --watermark: #f2f5f9;
    --on-blue: #ffffff;
  }
  * { margin: 0; padding: 0; box-sizing: border-box; }
  html, body { width: 927px; height: 1200px; overflow: hidden; background: var(--paper); }
  .letterhead {
    position: relative;
    width: 927px;
    height: 1200px;
    background: var(--paper);
    font-family: "Poppins", sans-serif;
    overflow: hidden;
  }
  .header-rule {
    position: absolute;
    left: 0; top: 154px;
    width: 520px; height: 2px;
    background: var(--brand-blue);
  }
  .contact-panel {
    position: absolute;
    left: 0; top: 0;
    width: 927px; height: 157px;
  }
  .brand {
    position: absolute;
    left: 112px; top: 52px;
    display: flex;
    align-items: center;
    gap: 16px;
  }
  .brand-dot {
    width: 40px; height: 40px;
    border-radius: 50%;
    background: var(--brand-blue);
  }
  .brand-name {
    font-size: 58px;
    font-weight: 500;
    line-height: 1;
    letter-spacing: 1px;
    color: var(--brand-blue);
  }
  .contact-list {
    position: absolute;
    left: 587px; top: 36px;
    list-style: none;
    color: var(--on-blue);
  }
  .contact-item {
    display: flex;
    align-items: flex-start;
    gap: 5px;
    margin-bottom: 14px;
  }
  .contact-item svg { flex: none; margin-top: 4px; }
  .contact-phone { font-size: 17px; font-weight: 700; line-height: 1.1; }
  .contact-address { font-size: 15.5px; font-weight: 500; line-height: 1.1; }
  .watermark {
    position: absolute;
    left: 0; top: 470px;
    width: 927px;
    text-align: center;
    font-size: 160px;
    font-weight: 500;
    color: var(--watermark);
    letter-spacing: 2px;
  }
  .footer-band {
    position: absolute;
    top: 1174px; height: 26px;
  }
  .footer-band--blue { left: 0; width: 461px; background: var(--brand-blue); }
  .footer-band--grey { left: 466px; width: 461px; background: var(--brand-grey); }
</style>
</head>
<body>
<div class="letterhead">
  <svg class="contact-panel" viewBox="0 0 927 157" aria-hidden="true">
    <polygon points="582,0 927,0 927,157 510,157" fill="var(--brand-blue)"/>
  </svg>
  <div class="header-rule"></div>

  <div class="brand">
    <span class="brand-dot"></span>
    <span class="brand-name">KESTROW</span>
  </div>

  <ul class="contact-list">
    <li class="contact-item contact-phone">
      <svg width="13" height="13" viewBox="0 0 24 24" aria-hidden="true">
        <path fill="none" stroke="#fff" stroke-width="2.4" stroke-linejoin="round" d="M6 3l3 5-2 2c1 3 4 6 7 7l2-2 5 3-2 3C11 21 3 13 3 5z"/>
      </svg>
      <span>+1 (212) 555 0147</span>
    </li>
    <li class="contact-item contact-phone">
      <svg width="13" height="13" viewBox="0 0 24 24" aria-hidden="true">
        <rect x="2" y="9" width="5" height="13" fill="none" stroke="#fff" stroke-width="2"/>
        <rect x="9" y="9" width="13" height="13" fill="none" stroke="#fff" stroke-width="2"/>
        <rect x="11" y="2" width="9" height="7" fill="none" stroke="#fff" stroke-width="2"/>
        <path d="M12 13h2M16 13h2M12 17h2M16 17h2" stroke="#fff" stroke-width="2"/>
      </svg>
      <span>+1 (212) 555 0182</span>
    </li>
    <li class="contact-item contact-address">
      <svg width="11" height="15" viewBox="0 0 20 28" aria-hidden="true">
        <path fill="#fff" d="M10 0C4.5 0 0 4.5 0 10c0 7 10 18 10 18s10-11 10-18C20 4.5 15.5 0 10 0zm0 14a4 4 0 110-8 4 4 0 010 8z"/>
      </svg>
      <span>482 W 71st Street 14th Floor<br>New York, NY 10157</span>
    </li>
  </ul>

  <div class="watermark" aria-hidden="true">KESTROW</div>

  <div class="footer-band footer-band--blue"></div>
  <div class="footer-band footer-band--grey"></div>
</div>
</body>
</html>
```